webdesign for a spectacles/glasses designer

Hello,

Someone in my village designs his own spectacles/eyeglasses.

For this I need a design that looks better than my poor design skills ;o)

The site is based around collections, subcollections and the actual items.

So we need a design that lists these in a nice way, worst case on seperate pages.

Here you can find the working material...

https://www.filevaultic.com/s/q7kmtr4p2wz91xb/BriefHarbor.zip

keep an eye on the product_tree file.

first level is the collection name
2nd is the model group
3rd is the model (on most of them it's just a different color of the same base model)

I added a seperate contact info file (line is too slow to reupload 60Mb again :( )

https://dl.filevaulticcontent.com/u/31906524/Anselm/contact.zip

I think I forgot to mention that it will be a shop like site to present his products,
altho I will add a cart system there won't be a payment system linked to it as
people who place orders will get contacted with payment instructions.
Updates

In the zipfile /Logo/logo_mistral_font.psd is the main logo
(you need to change character spacing to 1 to get rid of the spacing gaps)

the other one is only a collection logo

Target Market(s)

Plain customers and his resellers.

Industry/Entity Type

Shop

Requirements
Must have
• - a design that suits responsive behaviour (via the 960 grid)
- a menu is always handy (home, about, collections, contact)
- highlighted area/slider to highlight his sunglasses over glasses thingy
- featured products (newly added or promotional stuff)

there is a lot of pretty pictures to be supplied so do what you think is best

Nice to have
• a roll over zoom with selectable thumbnails or a plain gallery with full picture display at the product page.

maybe a drop down menu for the collection part (I will supply a screenshot of the backend structure)

```html
<!DOCTYPE html>
<html lang="en">
<head>
<meta charset="utf-8">
<title>Corvano — Eyewear</title>
<link rel="stylesheet" href="https://fonts.googleapis.com/css2?family=Questrial&family=Ubuntu:wght@400&family=Arimo:wght@400&display=swap">
<style>
  :root {
    --accent: #d9261c;
    --ink: #2a2a2a;
    --muted: #6a6a6a;
    --rule: #d6d6d6;
    --dot: #cfcfcf;
    --band: rgba(34,34,34,0.92);
    --footer-bg: #f1f1f1;
    --bottom-bg: #2d2d2d;
    --white: #ffffff;
  }
  * { box-sizing: border-box; margin: 0; padding: 0; }
  html, body { width: 938px; height: 1200px; overflow: hidden; background: var(--white); }
  body { position: relative; font-family: "Ubuntu", sans-serif; color: var(--ink); }
  .abs { position: absolute; }
  a { text-decoration: none; }

  /* header */
  .brand { left: 80px; top: 26px; font-family: "Ubuntu", sans-serif; font-size: 36px; font-weight: 400; color: #111; letter-spacing: 0.5px; }
  .cart { right: 86px; top: 15px; font-size: 10px; color: #8a8a8a; display: flex; align-items: center; gap: 3px; }
  .cart .count { background: #f0501e; color: #fff; padding: 1px 3px; font-weight: 700; font-family: "Arimo", sans-serif; }
  .cart .caret { width: 0; height: 0; border-left: 3px solid transparent; border-right: 3px solid transparent; border-top: 4px solid var(--accent); margin-left: 2px; }
  .nav { top: 48px; font-size: 11px; color: #333; }
  .nav.active { color: var(--accent); }
  .search { left: 667px; top: 44px; width: 186px; height: 22px; border: 1px solid #cfcfcf; background: #fff; }
  .search svg { position: absolute; right: 6px; top: 4px; }

  /* hero */
  .hero { left: 0; top: 82px; width: 938px; height: 381px; background: radial-gradient(ellipse at 55% 55%, #b59a84 0%, #8b7b70 30%, #6e6c6b 60%, #6a6a6a 100%); }
  .hero-arrow { top: 252px; }
  .pager { top: 434px; left: 425px; display: flex; gap: 8px; align-items: center; }
  .pager .btn { width: 14px; height: 14px; border-radius: 50%; background: #111; }
  .pager .pip { width: 5px; height: 5px; border-radius: 50%; background: #111; box-shadow: 0 0 0 1px rgba(255,255,255,.5); }
  .pager .pip.on { background: #fff; box-shadow: 0 0 0 2px #111; }

  /* section titles */
  .rule { height: 1px; background: var(--rule); }
  .rule-dot { width: 10px; height: 10px; border-radius: 50%; background: var(--dot); }
  .section-title { font-family: "Questrial", sans-serif; font-size: 25px; font-weight: 400; color: #222; white-space: nowrap; }

  /* product cards */
  .card { top: 560px; width: 168px; height: 210px; border: 1px solid #d2d2d2; background: #fff; }
  .card .photo { position: absolute; left: 3px; top: 3px; width: 160px; height: 203px; }
  .card .caption { position: absolute; left: 3px; bottom: 3px; width: 160px; height: 59px; background: var(--band); text-align: center; color: #fff; }
  .caption .code { font-family: "Questrial", sans-serif; color: var(--accent); font-size: 15px; margin-top: 5px; line-height: 16px; }
  .caption .name { font-size: 11.5px; line-height: 16px; }
  .caption .variant { font-family: "Arimo", sans-serif; font-size: 9px; line-height: 13px; }

  /* collections */
  .collection { top: 889px; width: 227px; height: 140px; }
  .collection .label { position: absolute; left: 0; bottom: 0; width: 100%; height: 27px; background: rgba(50,45,42,.82); color: #fff; font-size: 15.5px; padding: 4px 10px; }

  /* footer */
  .footer { left: 0; top: 1070px; width: 938px; height: 97px; background: var(--footer-bg); }
  .foot-head { top: 1085px; font-family: "Questrial", sans-serif; font-size: 18px; font-weight: 400; color: #333; padding-bottom: 2px; border-bottom: 1px solid #d4d4d4; width: 125px; }
  .foot-link { font-family: "Arimo", sans-serif; font-size: 11px; color: #555; }
  .news-input { left: 681px; top: 1123px; width: 168px; height: 24px; border: 1px solid #ddd; background: #fff; font-family: "Arimo", sans-serif; font-size: 10px; color: #999; padding: 6px 6px; }
  .news-btn { left: 800px; top: 1125px; width: 47px; height: 20px; background: #333; color: #fff; font-family: "Arimo", sans-serif; font-size: 10.5px; text-align: center; line-height: 20px; }
  .bottom { left: 0; top: 1167px; width: 938px; height: 33px; background: var(--bottom-bg); }
  .copyright { left: 84px; top: 1177px; font-family: "Arimo", sans-serif; font-size: 10.5px; color: #cfcfcf; }
  .social { top: 1176px; display: flex; gap: 8px; left: 748px; }
  .social span { width: 13px; height: 13px; border-radius: 50%; background: #e6e6e6; }
</style>
</head>
<body>

<header>
  <div class="abs brand">Corvano</div>
  <div class="abs cart">
    <svg width="12" height="10" viewBox="0 0 12 10"><path d="M0 1h2l2 6h6l1.5-4.5H3" fill="none" stroke="#8a8a8a" stroke-width="1.4"/><circle cx="4.5" cy="9" r="1" fill="#8a8a8a"/><circle cx="9" cy="9" r="1" fill="#8a8a8a"/></svg>
    Shopping Cart <span class="count">0 items</span> - £0<span class="caret"></span>
  </div>
  <nav>
    <a class="abs nav active" style="left:346px">Home</a>
    <a class="abs nav" style="left:422px">About</a>
    <a class="abs nav" style="left:496px">Collections <svg width="6" height="4" viewBox="0 0 6 4"><path d="M0.5 0.5L3 3l2.5-2.5" fill="none" stroke="#333"/></svg></a>
    <a class="abs nav" style="left:601px">Contact</a>
  </nav>
  <div class="abs search">
    <svg width="13" height="13" viewBox="0 0 13 13"><circle cx="5.5" cy="5.5" r="4" fill="none" stroke="#555" stroke-width="1.6"/><path d="M8.5 8.5L12 12" stroke="#555" stroke-width="1.8"/></svg>
  </div>
</header>

<section>
  <div class="abs hero" role="img" aria-label="Slider photo: model adjusting clip-on sunglasses over thin black-and-orange framed glasses"></div>
  <svg class="abs hero-arrow" style="left:20px" width="14" height="40" viewBox="0 0 14 40"><path d="M12 2L2 20l10 18" fill="none" stroke="#fff" stroke-width="2"/></svg>
  <svg class="abs hero-arrow" style="left:899px" width="14" height="40" viewBox="0 0 14 40"><path d="M2 2l10 18L2 38" fill="none" stroke="#fff" stroke-width="2"/></svg>
  <div class="abs pager">
    <span class="btn"></span><span class="pip on"></span><span class="pip"></span><span class="pip"></span><span class="btn"></span>
  </div>
</section>

<section>
  <div class="abs rule" style="left:80px;top:515px;width:250px"></div>
  <div class="abs rule-dot" style="left:327px;top:511px"></div>
  <h2 class="abs section-title" style="left:358px;top:500px">Featured Products</h2>
  <div class="abs rule-dot" style="left:583px;top:512px"></div>
  <div class="abs rule" style="left:590px;top:516px;width:261px"></div>

  <div class="abs card" style="left:80px">
    <div class="photo" role="img" aria-label="Product photo: model wearing red framed overlay sunglasses" style="background:linear-gradient(160deg,#6f6d6b,#9a8677 55%,#5f5d5c)"></div>
    <div class="caption"><div class="code">VLA07</div><div class="name">Stylish overlay sunglasses</div><div class="variant">Red Framed</div></div>
  </div>
  <div class="abs card" style="left:286px">
    <div class="photo" role="img" aria-label="Product photo: purple glasses frame close-up" style="background:linear-gradient(170deg,#f4f2f4,#e6e1e6 50%,#d9d4da)"></div>
    <div class="caption"><div class="code">KR31-Tn05</div><div class="name">Classy Glasses</div><div class="variant">Purple/red framed</div></div>
  </div>
  <div class="abs card" style="left:490px">
    <div class="photo" role="img" aria-label="Product photo: model wearing black framed overlay sunglasses" style="background:linear-gradient(160deg,#6f6d6b,#9a8677 55%,#5f5d5c)"></div>
    <div class="caption"><div class="code">VLA07</div><div class="name">Stylish overlay sunglasses</div><div class="variant">Black frames</div></div>
  </div>
  <div class="abs card" style="left:690px">
    <div class="photo" role="img" aria-label="Product photo: orange and red glasses temple close-up" style="background:linear-gradient(165deg,#f6f6f6 20%,#f0a020 45%,#e4401c 65%,#f4f4f4 90%)"></div>
    <div class="caption"><div class="code">KR28-Tn05</div><div class="name">Extra contoured glasses</div><div class="variant">Orange/red framed</div></div>
  </div>
</section>

<section>
  <div class="abs rule" style="left:90px;top:845px;width:265px"></div>
  <div class="abs rule-dot" style="left:354px;top:840px"></div>
  <h2 class="abs section-title" style="left:381px;top:829px">Our Collections</h2>
  <div class="abs rule-dot" style="left:565px;top:840px"></div>
  <div class="abs rule" style="left:572px;top:845px;width:293px"></div>

  <div class="abs collection" style="left:80px;background:linear-gradient(160deg,#6c6a68,#a08e80 50%,#4e4a47)" role="img" aria-label="Collection photo: model holding dark sunglasses">
    <div class="label">Sunglasses collection</div>
  </div>
  <div class="abs collection" style="left:354px;background:linear-gradient(160deg,#707070,#b09e8e 50%,#5c5854)" role="img" aria-label="Collection photo: model adjusting thin framed glasses">
    <div class="label">Sunglasses collection</div>
  </div>
  <div class="abs collection" style="left:630px;background:linear-gradient(160deg,#6a6a6a,#a4917f 40%,#565352)" role="img" aria-label="Collection photo: model holding several pairs of glasses">
    <div class="label">Sunglasses collection</div>
  </div>
</section>

<footer>
  <div class="abs footer"></div>
  <div class="abs foot-head" style="left:79px">Best sellers</div>
  <div class="abs foot-link" style="left:80px;top:1116px">Woman</div>
  <div class="abs foot-link" style="left:80px;top:1135px">Men</div>
  <div class="abs foot-head" style="left:274px">Eye glasses</div>
  <div class="abs foot-link" style="left:274px;top:1116px">Woman</div>
  <div class="abs foot-link" style="left:274px;top:1135px">Men</div>
  <div class="abs foot-head" style="left:493px">Sunglasses</div>
  <div class="abs foot-link" style="left:494px;top:1116px">Woman</div>
  <div class="abs foot-link" style="left:494px;top:1135px">Men</div>
  <div class="abs foot-head" style="left:680px;top:1083px">Newletter</div>
  <div class="abs news-input">Enter your email</div>
  <div class="abs news-btn">Submit</div>

  <div class="abs bottom"></div>
  <div class="abs copyright">Copyright © Corvano 2013 centered</div>
  <div class="abs social"><span></span><span></span><span></span><span></span><span></span></div>
</footer>

</body>
</html>
```